Child sleep consultant needs a flyer to attract new clients

We need a flyer that will attract the attention of parents with children between newborn and 3 years old who may be experiencing sleep issues. The flyer will be placed at places such as community centres, doctors room, play centres, etc.

Our business is called Quiet Moonbeam Nest and provides a sleep consultancy service. Our service essentially provides a routine for parents to follow and general advice. Our service is not medical advice.

We need the flyer to have an overall tone that is soft and peaceful however can catch the attention of parents who may be struggling on minimal sleep. We would like photos with minimal text. The colour we use is green.

We will provide the text to appear in the flyer once we have a better idea of the layout that we prefer for the flyer. The text however wont be extensive, just some catchy points.

We want to direct people to our website which is quietmoonbeamnest.com.au. We also have a facebook page, which is Quiet Moonbeam Nest.

We have a logo that we would like to appear on the flyer. We will attach the file once the uploader on pixel forum is fixed.

Our consultant is a certified Rest Compass consultant, which has a separate logo that should appear somewhere on the logo. I will attach this once the uploader is fixed.

When we print the flyer - we want to print A5 SIZE ... please make sure the formatting is OK for this size.

Target Market(s)

Mums and Dads with children between newborn and 3 years old.

Industry/Entity Type

Consultant

Colors
cadf82

Requirements
Must have
• - Our logo.
• - Rest Compass consultant logo - both attached to this brief.
• - Contact details - including phone number, email address and website
• - MUST be suitable for A5 printable size, double sided please.
• Must have the following text:
• If your baby or toddler isn't sleeping through the night, neither are you - and this means you are probably feeling physically and mentally exhausted, stressed, depressed and irritable, afraid you might be damaging your child and disconnected from your partner.
• The good news is nearly all healthy children 3 months or older are physically capable of sleeping 12 solid hours without waking. They just need to be taught the healthy sleep habits that enable them to do so.
• I can help with the sleep issues your child is experiencing. As a certified Rest Compass (insert trademark TM here) I can help if:
• - your child will only fall asleep when nursing or bottle feeding
• - your child needs a dummy in order fall asleep
• - you're waking up with your child one or more times per night
• - your child needs to be rocked, patted, or taken for a car ride to go to sleep
• - your own lack of sleep is starting to take a toll on your family
• I've been personally trained by Lorna Whitcaster, best selling author of the Rest Compass (insert trade mark symbol here) Program to teach her sleep training methods to families like yours. Lorna's methods have already helped over 30,000 parents and children and I'd be delighted to help your family next!
• Call or email for a free 15 minute consultation
• I would love to connect with you to talk about your child's specific situation and discuss different solutions.

```html
<!DOCTYPE html>
<html lang="en">
<head>
<meta charset="utf-8">
<title>Quiet Moonbeam Nest – A5 Flyer, Front and Back</title>
<link href="https://fonts.googleapis.com/css2?family=Roboto+Condensed:wght@300;400;700&display=swap" rel="stylesheet">
<style>
  :root{
    --backdrop:#1f5a86;
    --paper:#ffffff;
    --leaf:#cadf82;
    --leaf-soft:#dfe59a;
    --sage:#8cb57d;
    --forest:#5e8a4a;
    --deep-green:#4f8a3a;
    --logo-green:#9cbf78;
    --orange:#f29a1f;
    --ink:#1d1d1b;
    --ink-soft:#3a3a38;
  }
  *{box-sizing:border-box;margin:0;padding:0}
  html,body{width:1200px;height:1200px;overflow:hidden}
  body{background:var(--backdrop);font-family:"Roboto Condensed",sans-serif;color:var(--ink);position:relative}
  .flyer{position:absolute;width:554px;height:787px;background:var(--paper);overflow:hidden}
  .flyer--front{left:33px;top:183px}
  .flyer--back{left:621px;top:303px}
  .abs{position:absolute}

  /* front */
  .front-wash{left:0;top:0;width:554px;height:440px;background:linear-gradient(180deg,#e9f0c8 0%,#f6f9e8 45%,#ffffff 100%)}
  .brand{left:31px;top:30px;display:flex;align-items:center;gap:12px}
  .brand__dot{width:46px;height:46px;border-radius:50%;background:var(--logo-green)}
  .brand__name{font-weight:300;color:var(--logo-green);font-size:34px;line-height:31px}
  .photo-baby{left:87px;top:177px;width:256px;height:240px;border-radius:40% 50% 30% 20%;background:radial-gradient(ellipse at 45% 45%,#e7b59c 0%,#cfa28d 40%,#b9c4cf 75%,rgba(255,255,255,0) 100%)}
  .photo-circle{border-radius:50%;border:5px solid #fff;box-shadow:0 2px 6px rgba(0,0,0,.15)}
  .photo-man{left:319px;top:17px;width:200px;height:200px;background:radial-gradient(circle at 50% 45%,#c98f6d 0%,#8a6045 50%,#4b3a30 100%)}
  .photo-woman{left:307px;top:177px;width:212px;height:212px;background:radial-gradient(circle at 45% 55%,#e9e4dc 0%,#cbb79a 45%,#5a4a3c 100%)}
  .headline{left:0;top:438px;width:554px;text-align:center;color:var(--orange);font-weight:700}
  .headline__lead{font-size:24px;line-height:30px}
  .headline__main{font-size:37px;line-height:36px}
  .front-body{left:20px;top:554px;width:514px;text-align:center;font-size:19px;line-height:24px;color:var(--ink-soft)}
  .good-news{left:0;top:637px;width:554px;height:78px;background:var(--leaf-soft);padding:8px 22px;text-align:center;font-size:16px;line-height:20.5px}
  .front-footer{left:0;top:715px;width:554px;height:72px;background:var(--forest);border-top:3px solid #fff;display:flex;align-items:center;color:#fff}
  .front-footer__phone{margin-left:44px;font-size:35px;font-weight:700}
  .front-footer__contact{margin-left:40px;display:flex;flex-direction:column;line-height:22px}
  .front-footer__web{font-size:21px;font-weight:700}
  .front-footer__email{font-size:15px;font-weight:400}

  /* back */
  .help-band{left:0;top:0;width:553px;height:235px;background:var(--sage)}
  .help-title{left:0;top:36px;width:553px;text-align:center;font-size:21px;line-height:27px;font-weight:400}
  .help-list{left:40px;top:112px;list-style:none;font-size:15.5px;line-height:22.4px}
  .help-list li{display:flex;align-items:center;gap:7px}
  .help-list svg{width:16px;height:14px;flex:none}
  .photo-rest{left:299px;top:235px;width:254px;height:360px;background:linear-gradient(180deg,#f2d2bf 0%,#f7e4d8 40%,#f3f1ee 60%,#e8c9a8 80%,#ffffff 100%)}
  .photo-rest::before{content:"";position:absolute;left:-60px;top:0;width:90px;height:100%;background:linear-gradient(90deg,#fff,rgba(255,255,255,0))}
  .trained{left:42px;top:250px;width:320px;font-size:16px;line-height:22.4px}
  .connect{left:40px;top:419px;width:260px;font-size:16px;line-height:19.2px}
  .back-brand{left:107px;top:500px;display:flex;align-items:center;gap:8px}
  .back-brand__dot{width:32px;height:32px;border-radius:50%;background:var(--logo-green)}
  .back-brand__name{font-weight:300;color:var(--logo-green);font-size:23px;line-height:22px}
  .cta-band{left:0;top:585px;width:553px;height:138px}
  .badge{left:396px;top:567px;width:100px;height:100px;border-radius:50%;background:#fff}
  .cta-title{left:33px;top:615px;font-weight:700;font-size:26px;line-height:30px}
  .cta-sub{left:33px;top:647px;font-weight:700;font-size:23px;line-height:26px}
  .cta-note{left:33px;top:673px;font-weight:700;font-size:14.5px;line-height:19px}
  .cta-phone{left:335px;top:676px;font-weight:700;font-size:35px;color:var(--deep-green)}
  .back-footer{left:0;top:723px;width:553px;height:64px;background:var(--sage);display:flex;align-items:center;color:#fff}
  .back-footer__social{margin-left:44px;font-weight:300;font-size:15px;padding-right:14px;border-right:1px solid #fff;line-height:30px}
  .back-footer__web{margin-left:12px;font-weight:700;font-size:14.5px;letter-spacing:3.4px}
</style>
</head>
<body>

<section class="flyer flyer--front" aria-label="Flyer front">
  <div class="abs front-wash"></div>
  <div class="abs photo-baby" role="img" aria-label="Photo of a crying baby in a knitted hat"></div>
  <div class="abs photo-circle photo-man" role="img" aria-label="Photo of a tired man sitting on the edge of a bed"></div>
  <div class="abs photo-circle photo-woman" role="img" aria-label="Photo of an exhausted woman lying awake in bed"></div>
  <div class="abs brand">
    <span class="brand__dot"></span>
    <span class="brand__name">Quiet<br>Moonbeam<br>Nest</span>
  </div>

  <h1 class="abs headline">
    <span class="headline__lead">If your baby or toddler isn't</span><br>
    <span class="headline__main">sleeping through the night,<br>neither are you</span>
  </h1>
  <p class="abs front-body">This means you are probably feeling physically and mentally exhausted, stressed, depressed and irritable, afraid you might be damaging your child and disconnected from your partner.</p>
  <p class="abs good-news">The good news is nearly all healthy children 3 months or older are physically capable of sleeping 12 solid hours without waking. They just need to be taught the healthy sleep habits that enable them to do so.</p>
  <div class="abs front-footer">
    <span class="front-footer__phone">0491 570 156</span>
    <span class="front-footer__contact">
      <span class="front-footer__web">quietmoonbeamnest.com.au</span>
      <span class="front-footer__email">hello@quietmoonbeamnest.com.au</span>
    </span>
  </div>
</section>

<section class="flyer flyer--back" aria-label="Flyer back">
  <div class="abs help-band"></div>
  <h2 class="abs help-title">I can help with the sleep issues your child is experiencing.<br>As a certified Rest Compass&nbsp;™ I can help if:</h2>
  <ul class="abs help-list">
    <li><svg viewBox="0 0 16 14"><path d="M1 8 L6 13 L15 1" fill="none" stroke="#fff" stroke-width="3"/></svg>Your child will only fall asleep when nursing or bottle feeding</li>
    <li><svg viewBox="0 0 16 14"><path d="M1 8 L6 13 L15 1" fill="none" stroke="#fff" stroke-width="3"/></svg>Your child needs a dummy in order fall asleep</li>
    <li><svg viewBox="0 0 16 14"><path d="M1 8 L6 13 L15 1" fill="none" stroke="#fff" stroke-width="3"/></svg>You're waking up with your child one or more times per night</li>
    <li><svg viewBox="0 0 16 14"><path d="M1 8 L6 13 L15 1" fill="none" stroke="#fff" stroke-width="3"/></svg>Your child needs to be rocked, patted, or taken for a car ride to go to sleep</li>
    <li><svg viewBox="0 0 16 14"><path d="M1 8 L6 13 L15 1" fill="none" stroke="#fff" stroke-width="3"/></svg>Your own lack of sleep is starting to take a toll on your family</li>
  </ul>

  <div class="abs photo-rest" role="img" aria-label="Photos of a peacefully sleeping newborn and a sleeping mother on white pillows"></div>
  <p class="abs trained">I've been personally trained by Lorna Whitcaster,<br>best selling author of the Rest Compass&nbsp;™<br>Program to teach her sleep training methods<br>to families like yours. Lorna's methods have<br>already helped over 30,000 parents and<br>children and I'd be delighted to help your<br>family next!</p>
  <p class="abs connect">I would love to connect with you to<br>talk about your child's specific<br>situation and discuss different<br>solutions.</p>
  <div class="abs back-brand">
    <span class="back-brand__dot"></span>
    <span class="back-brand__name">Quiet<br>Moonbeam<br>Nest</span>
  </div>

  <svg class="abs cta-band" viewBox="0 0 553 138" preserveAspectRatio="none" aria-hidden="true">
    <path d="M0 26 C180 0 380 0 553 18 L553 138 L0 138 Z" fill="var(--leaf)"/>
  </svg>
  <div class="abs badge" aria-label="Certified consultant badge"></div>
  <p class="abs cta-title">CONTACT US FOR&nbsp; A</p>
  <p class="abs cta-sub">FREE 15 MINUTE CONSULTATION</p>
  <p class="abs cta-note">and take the first step to a full nights sleep.<br>Your little person is never too young to start.</p>
  <p class="abs cta-phone">0491 570 156</p>
  <div class="abs back-footer">
    <span class="back-footer__social">social.quietmoonbeamnest.com.au</span>
    <span class="back-footer__web">quietmoonbeamnest.com.au</span>
  </div>
</section>

</body>
</html>
```